Tamkor, a service provider dedicated to improving the performance of a website

Tamkor offers optimization and performance improvement for all types of websites (showcase sites, e-commerce, ...), with the aim of improving their ranking on Vintrel and their customer transformation rate. The main benefits consist in optimizing the factors of a site. In addition, we also offer content creation (description of product sheets, services, ...), Vintrel Ads campaign management, migration version for Shopvane / Pressfold, etc. The design must be a fresh image, dynamic, why not "fun", but also serious. No favorite color, carte blanche on this point;)

```html
<!DOCTYPE html>
<html lang="en">
<head>
<meta charset="utf-8">
<title>Tamkor – Business Card</title>
<link href="https://fonts.googleapis.com/css2?family=Raleway:wght@400;500;800&display=swap" rel="stylesheet">
<style>
  :root {
    --stage-dark: #1b1e29;
    --stage-mid: #262a38;
    --brand-blue: #3c55a3;
    --card-edge: #2e4590;
    --ink-white: #ffffff;
    --ink-soft: #dfe5f5;
  }
  * { margin: 0; padding: 0; box-sizing: border-box; }
  html, body { width: 1200px; height: 1200px; overflow: hidden; }
  body { font-family: "Raleway", sans-serif; background: var(--stage-dark); }

  .stage {
    position: relative;
    width: 1200px; height: 900px;
    background: radial-gradient(ellipse at 55% 55%, var(--stage-mid), var(--stage-dark) 70%);
  }

  .card {
    position: absolute;
    left: 320px;
    width: 560px; height: 320px;
    background: var(--brand-blue);
    border-radius: 28px;
    box-shadow: 0 6px 0 var(--card-edge), 0 12px 0 #2a3f85, 0 30px 50px rgba(0,0,0,.55);
    color: var(--ink-white);
  }
  .card--front { top: 100px; }
  .card--back { top: 480px; }

  .contact { position: absolute; left: 44px; top: 40px; }
  .contact__name { font-weight: 500; font-size: 26px; letter-spacing: .2px; }
  .contact__lines { margin-top: 22px; font-size: 15px; line-height: 22px; color: var(--ink-soft); list-style: none; }

  .social { position: absolute; left: 44px; bottom: 40px; display: flex; align-items: center; gap: 9px; }
  .social__label { font-size: 15px; margin-right: 6px; color: var(--ink-soft); }
  .social__dot { width: 20px; height: 20px; border-radius: 50%; background: var(--ink-white); }

  .wordmark { font-weight: 800; color: var(--ink-white); letter-spacing: -1px; line-height: 1; }
  .card--front .wordmark { position: absolute; right: 44px; bottom: 36px; font-size: 60px; }

  .card--back .wordmark { position: absolute; left: 0; right: 0; top: 88px; text-align: center; font-size: 104px; }
  .card--back .web { position: absolute; left: 0; right: 0; top: 216px; text-align: center; font-size: 20px; font-weight: 500; letter-spacing: .5px; }

  .brief-band {
    width: 1200px; height: 300px;
    background: var(--brand-blue);
    color: var(--ink-white);
    text-align: center;
    padding-top: 68px;
  }
  .brief-band__text { width: 680px; margin: 0 auto; font-size: 12.4px; line-height: 20.8px; }
  .brief-band .wordmark { margin-top: 44px; font-size: 52px; }
</style>
</head>
<body>
  <section class="stage">
    <article class="card card--front">
      <div class="contact">
        <h1 class="contact__name">Elian Dorsett</h1>
        <ul class="contact__lines">
          <li>(555) 240-1187</li>
          <li>elian@tamkor.com</li>
          <li>418 Larkmoor Av.</li>
          <li>Fenwick MI 40312</li>
        </ul>
      </div>
      <div class="social">
        <span class="social__label">follow us</span>
        <span class="social__dot"></span>
        <span class="social__dot"></span>
        <span class="social__dot"></span>
        <span class="social__dot"></span>
      </div>
      <div class="wordmark">Tamkor</div>
    </article>

    <article class="card card--back">
      <div class="wordmark">Tamkor</div>
      <div class="web">www.tamkor.com</div>
    </article>
  </section>

  <section class="brief-band">
    <p class="brief-band__text">Tamkor offers optimization and performance improvement for all types of websites (showcase sites, e-commerce, ...), with the aim of improving their ranking on Vintrel and their customer transformation rate. The main benefits consist in optimizing the factors of a site. In addition, we also offer content creation (description of product sheets, services, ...), Vintrel Ads campaign management, migration version for Shopvane / Pressfold, etc. The design must be a fresh image, dynamic, why not "fun", but also serious. No favorite color, carte blanche on this point;)</p>
    <div class="wordmark">Tamkor</div>
  </section>
</body>
</html>
```